Label Design DormaLux Capsules

Hello dear designers!

We run a brand for dietary supplements and are looking for a talented designer to help take our brand to the next level. We are planning to launch new products with fresh packaging and redesigned labels. Additionally, we would like to refresh our company logo to make it fit better on the packaging.

Important Info:

Our brand: PuraVeta – specializing in products for detoxification, sleep, and eye protection.
Our shop: www.puraveta-shop.at – currently offering two main products:
PuraVeta (Detox Tincture)
Ocula Shield Guard (Blue Light Filter Glasses)
Project Goal: Initially, we are looking for a label design for our new product DormaLux (sleep capsules). If we like the design, we would like to revise the label for our first product, PuraVeta, and potentially rework our logo to make it more compact and visually appealing on our packaging.

Design Preferences: We are fans of the design style of Varo Nutra and would love a design in a similar style – modern, clean, and premium – but with a unique touch that fits our brand. You will find some inspirations and ideas that we particularly like in the attachment.

Important:

Our packaging for DormaLux is an 8 OZ jar (similar to the smaller jars used by Varo Nutra).
The label should be clear, appealing, and give the product a high-quality look.
An example of a previous design draft (which hasn’t fully convinced us yet), along with inspirations for our upcoming bundle (including PuraVeta, DormaLux, and OculaShield Guard), is also attached.
Special Opportunity: The designer with the best concept will have the chance to collaborate with us long-term! We have two more brands in the pipeline and are looking for a reliable and creative partner for future projects. Generous compensation and tips are guaranteed.

We look forward to seeing creative and professional designs that will take our brand to the next level!

Target Market(s)

Germany

Industry/Entity Type

Supplement

Font styles to use
Sans Serif

Colors

Designer to choose colors to be used in the design.

Requirements
Must have
• Es sollte Hochwertig und Modern aussehen. Matt schwarzer hintergrund. less is more
Nice to have
• Maybe The head should be visible in the background.
Should not have
• it should not be colorful, and not too playful, it should definitely not look cheap!

```html
<!DOCTYPE html>
<html lang="de">
<head>
<meta charset="utf-8">
<title>DormaLux – Etikett</title>
<link href="https://fonts.googleapis.com/css2?family=Bebas+Neue&family=Oswald:wght@400;500;600&display=swap" rel="stylesheet">
<style>
  :root{
    --label-black:#1c1c1c;
    --deep-black:#0e0e0e;
    --band-grey:#262626;
    --headline-white:#f4f4f4;
    --text-white:#e9e9e9;
    --accent-cyan:#22c8ea;
    --brand-gold:#c9a45c;
    --page-bg:#f5f5f5;
  }
  html,body{margin:0;padding:0;overflow:hidden;background:var(--page-bg);}
  .label{
    position:relative;width:1200px;height:610px;overflow:hidden;
    background:linear-gradient(180deg,var(--label-black) 0%,#202020 60%,#181818 100%);
    font-family:"Oswald",sans-serif;color:var(--text-white);
  }
  .head-motif{
    position:absolute;left:370px;top:40px;width:470px;height:520px;
    border-radius:48% 52% 30% 40%;
    background:radial-gradient(ellipse at 55% 40%,rgba(255,255,255,.07) 0%,rgba(255,255,255,.03) 45%,rgba(255,255,255,0) 70%);
  }
  .brand-tab{
    position:absolute;left:545px;top:0;width:110px;height:118px;
    background:var(--deep-black);border-radius:0 0 55px 55px;
    display:flex;align-items:center;justify-content:center;
  }
  .brand-dot{width:34px;height:34px;border-radius:50%;border:2px solid var(--brand-gold);box-sizing:border-box;}
  .brand-name{
    position:absolute;top:134px;left:0;width:100%;text-align:center;
    font-weight:400;font-size:26px;letter-spacing:6px;color:var(--brand-gold);
  }
  .product-name{
    position:absolute;top:168px;left:0;width:100%;text-align:center;margin:0;
    font-family:"Bebas Neue",sans-serif;font-weight:400;font-size:138px;line-height:1;
    color:var(--headline-white);letter-spacing:1px;
  }
  .claim{
    position:absolute;top:314px;left:50%;transform:translateX(-50%);
    padding:4px 30px;border:2px solid var(--accent-cyan);border-radius:30px;
    font-family:"Oswald",sans-serif;font-weight:600;font-style:italic;font-size:32px;
    color:var(--accent-cyan);white-space:nowrap;letter-spacing:.5px;
  }
  .benefits{
    position:absolute;top:405px;left:0;width:100%;margin:0;padding:0;list-style:none;
    display:flex;flex-direction:column;align-items:center;gap:8px;
  }
  .benefits li{
    font-weight:500;font-size:21px;line-height:28px;padding-left:16px;
    border-left:3px solid var(--accent-cyan);width:335px;box-sizing:border-box;
  }
  .content-band{
    position:absolute;top:538px;left:470px;width:260px;height:46px;
    background:var(--band-grey);border-radius:8px;
    display:flex;align-items:center;justify-content:center;
    font-weight:500;font-size:21px;letter-spacing:.5px;
  }
  .content-band .divider{width:2px;height:22px;background:var(--accent-cyan);margin:0 8px;}
</style>
</head>
<body>
<div class="label">
  <div class="head-motif" role="img" aria-label="Dezente Kopfsilhouette mit Schaltkreislinien im Hintergrund"></div>
  <div class="brand-tab"><span class="brand-dot"></span></div>
  <div class="brand-name">PURAVETA</div>
  <h1 class="product-name">DORMALUX</h1>
  <div class="claim">FÖRDERT DIE TIEFSCHLAFPHASE</div>
  <ul class="benefits">
    <li>ZWISCHENÜBERSCHRIFT HINZUFÜGEN</li>
    <li>ZWISCHENÜBERSCHRIFT HINZUFÜGEN</li>
    <li>ZWISCHENÜBERSCHRIFT HINZUFÜGEN</li>
  </ul>
  <div class="content-band"><span>30 PORTIONEN</span><span class="divider"></span><span>60 KAPSELN</span></div>
</div>
</body>
</html>
```